Boutique Real Estate Brokerage looking for business card, letterhead and envelope design

We are looking for a cohesive design for our business cards, letterhead and envelopes and that mirrors our high-end homes and clientele. Fern & Gable is being launched and designed for the marketplace of tomorrow. We grew from the #1 team in our community into a full-service firm that is going to revolutionize the traditional real estate model.

We understand that it’s more important than ever to help our clients and partners adapt to behavioral and market changes being driven by generational shifts and technological advances in society, and by combining traditional brokerage services with innovative production and marketing capabilities, we know how to do that better than anyone else.

Requirements
Must have
• business card, letterhead and envelope design - attached logo.

```html
<!DOCTYPE html>
<html lang="en">
<head>
<meta charset="utf-8">
<title>Fern &amp; Gable Realty — Stationery</title>
<link href="https://fonts.googleapis.com/css2?family=Montserrat:wght@700&family=Questrial&display=swap" rel="stylesheet">
<style>
  :root{
    --backdrop:#363b47;
    --navy:#1a0b5c;
    --gold:#b98546;
    --gold-dark:#8a6440;
    --paper:#ffffff;
    --ink:#4a4a55;
  }
  *{margin:0;padding:0;box-sizing:border-box}
  html,body{width:1200px;height:828px;overflow:hidden;background:var(--backdrop)}
  .canvas{position:relative;width:1200px;height:828px;background:var(--backdrop)}
  .sheet{position:absolute;background:var(--paper);overflow:hidden}
  .sheet > .shapes{position:absolute;inset:0;width:100%;height:100%}
  .sprite{position:absolute;width:0;height:0;overflow:hidden}

  .letterhead{left:186px;top:153px;width:400px;height:518px}
  .envelope{left:619px;top:487px;width:371px;height:187px}
  .card{width:148px;height:85px}
  .card-a{left:639px;top:214px}
  .card-b{left:815px;top:214px}
  .card-c{left:639px;top:327px}
  .card-d{left:815px;top:327px}

  .brand{position:absolute;display:flex;align-items:center;gap:.45em;
    font-family:"Montserrat",sans-serif;font-weight:700;color:var(--navy);
    white-space:nowrap;letter-spacing:.01em}
  .brand .mark{width:.95em;height:.95em;background:var(--gold);flex:none}
  .brand.on-dark{color:var(--paper)}
  .letterhead .brand{left:18px;top:22px;font-size:16px}
  .envelope .brand{left:19px;top:19px;font-size:15px}
  .card-front .brand{left:54px;top:37px;font-size:8.5px}
  .card-back .brand{left:37px;top:12px;font-size:6.5px}

  .contact{position:absolute;display:flex;align-items:center;gap:7px;
    font-family:"Questrial",sans-serif;color:var(--ink);white-space:nowrap}
  .contact svg{flex:none}
  .letterhead .contact,.envelope .contact{font-size:6.6px}
  .letterhead .contact svg,.envelope .contact svg{width:9px;height:9px}
  .card-back .contact{font-size:4px;gap:5px;left:44px}
  .card-back .contact svg{width:5.5px;height:5.5px}
</style>
</head>
<body>
<svg class="sprite" aria-hidden="true">
  <defs>
    <linearGradient id="goldFade" x1="0" y1="0" x2="0" y2="1">
      <stop offset="0" stop-color="var(--gold-dark)" style="stop-color:#8a6440"/>
      <stop offset="1" stop-color="#b98546"/>
    </linearGradient>
    <symbol id="icon-phone" viewBox="0 0 20 20">
      <circle cx="10" cy="10" r="10" fill="#1a0b5c"/>
      <path d="M6.5 5.5l2 0 .8 2.5-1.2 1a6 6 0 0 0 3 3l1-1.2 2.5.8v2c0 .6-.5 1-1 1A9 9 0 0 1 5.5 6.5c0-.5.4-1 1-1z" fill="#fff"/>
    </symbol>
    <symbol id="icon-pin" viewBox="0 0 20 20">
      <circle cx="10" cy="10" r="10" fill="#1a0b5c"/>
      <path d="M10 4.5a4 4 0 0 0-4 4c0 3 4 7 4 7s4-4 4-7a4 4 0 0 0-4-4z" fill="#fff"/>
      <circle cx="10" cy="8.5" r="1.5" fill="#1a0b5c"/>
    </symbol>
    <symbol id="icon-globe" viewBox="0 0 20 20">
      <circle cx="10" cy="10" r="10" fill="#1a0b5c"/>
      <g fill="none" stroke="#fff" stroke-width="1">
        <circle cx="10" cy="10" r="4.5"/><ellipse cx="10" cy="10" rx="2" ry="4.5"/>
        <path d="M5.5 10h9"/>
      </g>
    </symbol>
    <symbol id="icon-mail" viewBox="0 0 20 20">
      <circle cx="10" cy="10" r="10" fill="#1a0b5c"/>
      <rect x="5.5" y="6.5" width="9" height="7" fill="#fff"/>
      <path d="M5.5 6.5l4.5 4 4.5-4" fill="none" stroke="#1a0b5c" stroke-width="1"/>
    </symbol>
  </defs>
</svg>

<main class="canvas">

  <section class="sheet letterhead" aria-label="Letterhead">
    <svg class="shapes" viewBox="0 0 400 518" preserveAspectRatio="none" aria-hidden="true">
      <polygon points="336,0 400,0 400,86" fill="var(--navy)"/>
      <polygon points="0,404 0,518 85,518" fill="url(#goldFade)"/>
    </svg>
    <div class="brand"><span class="mark"></span>FERN &amp; GABLE</div>
    <div class="contact" style="left:118px;top:482px"><svg><use href="#icon-phone"/></svg>+14035550187</div>
    <div class="contact" style="left:118px;top:495px"><svg><use href="#icon-pin"/></svg>42 Linden Crescent NW Halden</div>
    <div class="contact" style="left:272px;top:482px"><svg><use href="#icon-globe"/></svg>www.ferngable.example</div>
    <div class="contact" style="left:272px;top:495px"><svg><use href="#icon-mail"/></svg>hello@ferngable.example</div>
  </section>

  <section class="sheet card card-front card-a" aria-label="Business card front">
    <svg class="shapes" viewBox="0 0 148 85" preserveAspectRatio="none" aria-hidden="true">
      <rect width="148" height="85" fill="var(--navy)"/>
      <polygon points="116,0 148,0 148,41" fill="var(--paper)"/>
      <polygon points="0,0 0,85 64,85" fill="url(#goldFade)"/>
    </svg>
    <div class="brand on-dark"><span class="mark"></span>FERN &amp; GABLE</div>
  </section>

  <section class="sheet card card-back card-b" aria-label="Business card back">
    <svg class="shapes" viewBox="0 0 148 85" preserveAspectRatio="none" aria-hidden="true">
      <polygon points="117,0 148,0 148,41" fill="var(--navy)"/>
      <polygon points="0,24 0,85 46,85" fill="url(#goldFade)"/>
    </svg>
    <div class="brand"><span class="mark"></span>FERN &amp; GABLE</div>
    <div class="contact" style="top:37px"><svg><use href="#icon-phone"/></svg>+14035550187</div>
    <div class="contact" style="top:45.5px"><svg><use href="#icon-pin"/></svg>42 Linden Crescent NW Halden</div>
    <div class="contact" style="top:54px"><svg><use href="#icon-globe"/></svg>www.ferngable.example</div>
    <div class="contact" style="top:62.5px"><svg><use href="#icon-mail"/></svg>hello@ferngable.example</div>
  </section>

  <section class="sheet card card-back card-c" aria-label="Business card back">
    <svg class="shapes" viewBox="0 0 148 85" preserveAspectRatio="none" aria-hidden="true">
      <polygon points="117,0 148,0 148,41" fill="var(--navy)"/>
      <polygon points="0,24 0,85 46,85" fill="url(#goldFade)"/>
    </svg>
    <div class="brand"><span class="mark"></span>FERN &amp; GABLE</div>
    <div class="contact" style="top:37px"><svg><use href="#icon-phone"/></svg>+14035550187</div>
    <div class="contact" style="top:45.5px"><svg><use href="#icon-pin"/></svg>42 Linden Crescent NW Halden</div>
    <div class="contact" style="top:54px"><svg><use href="#icon-globe"/></svg>www.ferngable.example</div>
    <div class="contact" style="top:62.5px"><svg><use href="#icon-mail"/></svg>hello@ferngable.example</div>
  </section>

  <section class="sheet card card-front card-d" aria-label="Business card front">
    <svg class="shapes" viewBox="0 0 148 85" preserveAspectRatio="none" aria-hidden="true">
      <rect width="148" height="85" fill="var(--navy)"/>
      <polygon points="116,0 148,0 148,41" fill="var(--paper)"/>
      <polygon points="0,0 0,85 64,85" fill="url(#goldFade)"/>
    </svg>
    <div class="brand on-dark"><span class="mark"></span>FERN &amp; GABLE</div>
  </section>

  <section class="sheet envelope" aria-label="Envelope">
    <svg class="shapes" viewBox="0 0 371 187" preserveAspectRatio="none" aria-hidden="true">
      <polygon points="329,0 371,0 371,55" fill="var(--navy)"/>
      <polygon points="0,108 0,187 60,187" fill="url(#goldFade)"/>
    </svg>
    <div class="brand"><span class="mark"></span>FERN &amp; GABLE</div>
    <div class="contact" style="left:93px;top:155px"><svg><use href="#icon-phone"/></svg>+14035550187</div>
    <div class="contact" style="left:93px;top:168px"><svg><use href="#icon-pin"/></svg>42 Linden Crescent NW Halden</div>
    <div class="contact" style="left:247px;top:155px"><svg><use href="#icon-globe"/></svg>www.ferngable.example</div>
    <div class="contact" style="left:247px;top:168px"><svg><use href="#icon-mail"/></svg>hello@ferngable.example</div>
  </section>

</main>
</body>
</html>
```